Brightmoor Law Letterhead for Law firm must be modern and use the logo I uploaded.

Hello I want a clean modern professional letterhead for my law firm Brightmoor Law. A logo has already been created and all files have been uploaded. The information for the firm can be given through message. Please use the logo that has already been created. Please also use the color scheme of that logo. (blue and white).

Target Market(s)

General Public

Industry/Entity Type

Law Firm

Colors

Designer to choose colors to be used in the design.

Requirements
Must have
• This must be a modern professional letterhead
Nice to have
• My logo that is included in file form
Should not have
• Should not have logo that is not the one I uploaded.

```html
<!DOCTYPE html>
<html lang="en">
<head>
<meta charset="utf-8">
<title>Brightmoor Law Letterhead</title>
<link href="https://fonts.googleapis.com/css2?family=Roboto:wght@500&family=Arimo:wght@400&display=swap" rel="stylesheet">
<style>
  :root {
    --navy: #2b3164;
    --backdrop: #dcdcdc;
    --paper: #ffffff;
    --ink-muted: #555a66;
    --rule: #8a8d96;
  }
  * { margin: 0; padding: 0; box-sizing: border-box; }
  html, body {
    width: 1189px;
    height: 1200px;
    overflow: hidden;
    background: var(--backdrop);
  }
  .letterhead {
    position: absolute;
    left: 191px;
    top: 30px;
    width: 806px;
    height: 1140px;
    background: var(--paper);
  }
  .brand {
    position: absolute;
    top: 64px;
    left: 0;
    width: 100%;
    display: flex;
    flex-direction: column;
    align-items: center;
  }
  .brand-square {
    width: 40px;
    height: 40px;
    background: var(--navy);
  }
  .brand-name {
    margin-top: 28px;
    font-family: "Roboto", sans-serif;
    font-weight: 500;
    font-size: 15px;
    letter-spacing: 0.42em;
    margin-right: -0.42em;
    color: var(--navy);
    text-transform: uppercase;
  }
  .contact-footer {
    position: absolute;
    left: 195px;
    width: 416px;
    top: 1072px;
    font-family: "Arimo", sans-serif;
    color: var(--ink-muted);
  }
  .contact-address {
    text-align: center;
    font-size: 12.4px;
    padding-bottom: 5px;
    border-bottom: 1px solid var(--rule);
  }
  .contact-list {
    list-style: none;
    display: flex;
    justify-content: space-between;
    gap: 12px;
    margin-top: 6px;
    font-size: 12.4px;
  }
  .contact-item {
    display: flex;
    align-items: center;
    gap: 6px;
    white-space: nowrap;
  }
  .contact-icon {
    flex: none;
    width: 10px;
    height: 10px;
    fill: var(--navy);
  }
</style>
</head>
<body>
  <main class="letterhead">
    <header class="brand">
      <div class="brand-square"></div>
      <div class="brand-name">Brightmoor Law</div>
    </header>

    <footer class="contact-footer">
      <p class="contact-address">Your address, city, state, ZIP 0000</p>
      <ul class="contact-list">
        <li class="contact-item">
          <svg class="contact-icon" viewBox="0 0 24 24" aria-hidden="true"><path d="M6.6 10.8a15.1 15.1 0 0 0 6.6 6.6l2.2-2.2a1 1 0 0 1 1-.25 11.4 11.4 0 0 0 3.6.57 1 1 0 0 1 1 1V20a1 1 0 0 1-1 1A17 17 0 0 1 3 4a1 1 0 0 1 1-1h3.5a1 1 0 0 1 1 1c0 1.25.2 2.45.57 3.6a1 1 0 0 1-.25 1z"/></svg>
          <span>555-382-0147</span>
        </li>
        <li class="contact-item">
          <svg class="contact-icon" viewBox="0 0 24 24" aria-hidden="true"><path d="M2 5h20L12 12.5z"/><path d="M2 7.2l10 7.6 10-7.6V19H2z"/></svg>
          <span>youremail@brightmoor.com</span>
        </li>
        <li class="contact-item">
          <svg class="contact-icon" viewBox="0 0 24 24" aria-hidden="true"><circle cx="12" cy="12" r="10"/><path d="M2 12h20M12 2c3 3 3 17 0 20M12 2c-3 3-3 17 0 20" fill="none" stroke="#ffffff" stroke-width="1.6"/></svg>
          <span>www.brightmoor.com</span>
        </li>
      </ul>
    </footer>
  </main>
</body>
</html>
```